Offshore Energy Projects Management Consultancy needs a business card design

Logo available. We provide teams to deliver engineering consultancy, project management and delivery teams mainly in the offshore renewables sector. The company is all about bringing the right people to a project to deliver the scope.

The business card will be used for all staff.

The business card should be quite simple, vibrant and uncluttered but convey experience, enthusiasm and integration.

Target Market(s)

Energy Project Developers and Tier 1 construction companies

Contact Information for Business Card

Logo should be on the back of the card. I'm happy for the designer to play with the colour of the logo and background colour.

Front of the card should convey all the must have information in a clear and professional manner but without being overly traditional.

Colors

Designer to choose colors to be used in the design.

Requirements
Must have
• Land Line Tel Number, Mobile Tel Number, Email, business address, web address.

```html
<!DOCTYPE html>
<html lang="en">
<head>
<meta charset="utf-8">
<title>Tideline Project Partners – Business Card</title>
<link href="https://fonts.googleapis.com/css2?family=Open+Sans:wght@400;600;700&display=swap" rel="stylesheet">
<style>
  :root {
    --backdrop: #dcdcdc;
    --card: #fbfbfb;
    --edge: #1a74c0;
    --brand-blue: #2a9bd9;
    --deep-blue: #1f6fb8;
    --text-grey: #5e5f61;
  }
  * { box-sizing: border-box; margin: 0; padding: 0; }
  html, body {
    width: 1200px; height: 856px; overflow: hidden;
    background: var(--backdrop);
    font-family: "Open Sans", Arial, sans-serif;
  }
  .stage {
    width: 1200px; height: 856px;
    display: flex; align-items: center; justify-content: center; gap: 40px;
  }
  .card {
    width: 540px; height: 330px;
    background: var(--card);
    border-bottom: 5px solid var(--edge);
    position: relative;
  }
  /* Front */
  .card--front { display: flex; align-items: center; }
  .brand {
    display: flex; align-items: center; gap: 10px;
    color: var(--text-grey); font-weight: 600;
  }
  .brand__dot { width: 18px; height: 18px; border-radius: 50%; background: var(--deep-blue); flex: none; }
  .card--front .brand { width: 250px; padding-left: 34px; font-size: 19px; line-height: 1.2; }
  .divider { width: 2px; height: 170px; background: var(--deep-blue); margin-right: 28px; }
  .contact { color: var(--text-grey); font-size: 13.5px; line-height: 1.35; }
  .contact__name { color: var(--brand-blue); font-weight: 700; font-size: 19px; line-height: 1.1; }
  .contact__role { font-size: 16px; margin-bottom: 10px; }
  .contact__address-lead { color: var(--brand-blue); }
  .contact__lines { list-style: none; margin-top: 10px; }
  .contact__lines li { display: flex; align-items: center; gap: 10px; }
  .contact__lines svg { width: 13px; height: 13px; fill: var(--brand-blue); flex: none; }
  /* Back */
  .card--back { display: flex; flex-direction: column; align-items: center; justify-content: center; }
  .card--back .brand { font-size: 30px; gap: 14px; }
  .card--back .brand__dot { width: 26px; height: 26px; }
  .web { position: absolute; bottom: 40px; color: var(--brand-blue); font-size: 15px; }
</style>
</head>
<body>
<main class="stage">
  <section class="card card--front" aria-label="Card front">
    <div class="brand"><span class="brand__dot"></span><span>Tideline Project Partners</span></div>
    <div class="divider"></div>
    <div class="contact">
      <p class="contact__name">Martin Calloway</p>
      <p class="contact__role">Director</p>
      <p class="contact__address-lead">The Harbour Building,</p>
      <p>210 Quay Road,</p>
      <p>Northport, NP4 2GE</p>
      <ul class="contact__lines">
        <li><svg viewBox="0 0 24 24" aria-hidden="true"><path d="M6.6 10.8a15 15 0 0 0 6.6 6.6l2.2-2.2a1 1 0 0 1 1-.25 11.4 11.4 0 0 0 3.6.57 1 1 0 0 1 1 1V20a1 1 0 0 1-1 1A17 17 0 0 1 3 4a1 1 0 0 1 1-1h3.5a1 1 0 0 1 1 1c0 1.25.2 2.45.57 3.57a1 1 0 0 1-.25 1z"/></svg>+44 1632 960 118</li>
        <li><svg viewBox="0 0 24 24" aria-hidden="true"><path d="M7 1h10a2 2 0 0 1 2 2v18a2 2 0 0 1-2 2H7a2 2 0 0 1-2-2V3a2 2 0 0 1 2-2zm0 3v14h10V4zm5 15.5a1 1 0 1 0 0 2 1 1 0 0 0 0-2z"/></svg>+44 7700 900 412</li>
        <li><svg viewBox="0 0 24 24" aria-hidden="true"><path d="M2 5h20v14H2zm2 2v.5l8 5 8-5V7zm0 2.8V17h16V9.8l-8 5z"/></svg>hello@tidelinepm.co</li>
        <li><svg viewBox="0 0 24 24" aria-hidden="true"><path d="M12 2a10 10 0 1 0 0 20 10 10 0 0 0 0-20zm6.9 9h-3a15 15 0 0 0-1.3-6A8 8 0 0 1 18.9 11zM12 4.1c.9 1.3 1.7 3.6 1.9 6.9h-3.8c.2-3.3 1-5.6 1.9-6.9zM9.4 5A15 15 0 0 0 8.1 11h-3A8 8 0 0 1 9.4 5zM5.1 13h3a15 15 0 0 0 1.3 6A8 8 0 0 1 5.1 13zm6.9 6.9c-.9-1.3-1.7-3.6-1.9-6.9h3.8c-.2 3.3-1 5.6-1.9 6.9zm2.6-.9a15 15 0 0 0 1.3-6h3a8 8 0 0 1-4.3 6z"/></svg>www.tidelinepm.co</li>
      </ul>
    </div>
  </section>

  <section class="card card--back" aria-label="Card back">
    <div class="brand"><span class="brand__dot"></span><span>Tideline Project Partners</span></div>
    <p class="web">www.tidelinepm.co</p>
  </section>
</main>
</body>
</html>
```